A website for a Maltese Law Firm

Our law firm needs a website to further its business. The site should have a simple yet effective design. We would need the following sections: About us, Practice Areas, About Malta, Contact. These should be further split as follows:

About us: Our firm, Our values, What others say, Offices

Practice Areas: Crimimal, Citizenship & Residence, Harbour Passage Scheme, Criminal Defence, Civil Litigation, Arbitration and ADR, Commercial and Corporate, Media Law.

About Malta: just one section.

Contact: Just one section

We would also need a news feed at the front of the site to include latest news regarding our cases.

At the bottom we need a section for our Terms and a Privacy Statement.

Our logo is being attached.

Target Market(s)

All clients looking for legal assistance in Malta

Industry/Entity Type

Legal

Coding

Coded - Design and coding required

Number of Pages Required

1 page

Requirements
Must have
• It must be simple yet striking.

```html
<!DOCTYPE html>
<html lang="en">
<head>
<meta charset="utf-8">
<title>Vellamar &amp; Costain Advocates</title>
<link href="https://fonts.googleapis.com/css2?family=Oswald:wght@400;500&family=Roboto:ital,wght@0,400;0,500;0,700;1,400&display=swap" rel="stylesheet">
<style>
:root{
  --accent:#2a97c0;
  --ink:#222;
  --text:#555;
  --muted:#777;
  --line:#d8d8d8;
  --band:#eeeeee;
  --band-light:#f4f4f4;
  --footer:#454545;
  --footer-bottom:#1c1c1c;
  --white:#fff;
}
*{box-sizing:border-box;margin:0;padding:0}
html,body{width:1200px;height:2782px;overflow:hidden}
body{position:relative;background:var(--white);font-family:'Roboto',sans-serif;color:var(--text)}
.abs{position:absolute}
.accent{color:var(--accent)}

/* header */
.site-header{left:0;top:0;width:1200px;height:115px;background:var(--white);box-shadow:0 2px 6px rgba(0,0,0,.12);z-index:2}
.brand{left:90px;top:43px;font-family:'Roboto',sans-serif;font-weight:500;color:var(--ink);font-size:24px;line-height:28px;letter-spacing:.5px}
.main-nav{left:483px;top:0;height:115px;display:flex;font-size:16px;text-transform:uppercase;color:var(--ink)}
.main-nav a{display:flex;align-items:center;padding:0 14px;height:115px;color:inherit;text-decoration:none}
.main-nav a.active{background:var(--accent);color:var(--white);width:98px;justify-content:center}

/* hero */
.hero{left:0;top:115px;width:1200px;height:575px;background:linear-gradient(90deg,#cfd7dc 0%,#9fb0ba 35%,#6a7f8d 60%,#3a3f45 75%,#2d3036 100%)}
.hero-card{left:90px;top:326px;width:510px;height:230px;background:rgba(255,255,255,.55);padding:30px 38px}
.hero-card h1{font-family:'Oswald',sans-serif;font-weight:400;font-size:48px;line-height:54px;color:var(--accent);letter-spacing:.5px}
.hero-card p{font-family:'Oswald',sans-serif;font-size:24px;color:#333;margin-top:4px}
.btn-dark{display:inline-block;margin-top:18px;background:#1e1e1e;color:var(--white);font-size:23px;padding:14px 28px;border-radius:5px}

/* quick links */
.quick-bar{left:0;top:690px;width:1200px;height:122px;background:var(--band-light)}
.quick{top:18px;height:84px;border:2px solid #9ccfe1;background:var(--white);display:flex;align-items:center;justify-content:center;gap:14px;font-size:20px;text-transform:uppercase;color:var(--accent)}

/* section headings */
.h-section{font-size:24px;color:var(--ink);text-transform:uppercase;font-weight:400}
.center{text-align:center;width:1200px;left:0}

.welcome-text{left:160px;top:900px;width:880px;text-align:center;font-size:14.5px;line-height:26px;color:var(--muted)}

/* practice */
.arrows{top:1013px;left:1037px;display:flex;gap:8px}
.arrows span{width:32px;height:30px;border:1px solid var(--line);display:flex;align-items:center;justify-content:center}
.practice{top:1071px;width:240px;height:300px;text-align:center}
.practice.featured{border:1px solid #cfcfcf;box-shadow:0 3px 8px rgba(0,0,0,.2);background:var(--white)}
.practice .icon{width:94px;height:94px;margin:38px auto 0;border-radius:50%;border:1px solid #777;display:flex;align-items:center;justify-content:center}
.practice.featured .icon{background:var(--accent);border-color:var(--accent)}
.practice h3{font-size:14px;font-weight:400;text-transform:uppercase;color:var(--ink);margin-top:26px}
.practice.featured h3{color:var(--accent)}
.practice p{font-size:12.5px;line-height:18px;color:#555;width:206px;margin:8px auto 0}
.more{display:inline-block;margin-top:14px;font-size:11px;border:1px solid #333;border-radius:3px;padding:4px 10px;color:#333}
.practice.featured .more{border-color:var(--accent);color:var(--accent)}

/* law office */
.office-band{left:0;top:1421px;width:1200px;height:320px;background:var(--band)}
.office-list{left:92px;top:1520px;list-style:none;font-size:14.5px;color:#555}
.office-list li{height:34px;display:flex;gap:10px}
.office-list li::before{content:"»";color:var(--accent);font-weight:700}
.photo{border:4px solid var(--white);box-shadow:0 0 0 1px #ccc}

/* news */
.news{top:1855px;width:318px}
.news .img{height:193px;position:relative}
.date{position:absolute;left:0;top:50px;width:46px;text-align:center;color:var(--white)}
.date .d{background:var(--accent);font-size:22px;line-height:30px}
.date .m{background:var(--accent);font-size:10px;line-height:14px;padding-bottom:4px}
.date .y{background:#2b2b2b;font-size:14px;line-height:32px}
.news h4{font-size:17px;font-weight:400;color:var(--ink);margin-top:16px}
.news p{font-size:12px;line-height:19px;color:#555;margin-top:8px}

/* team */
.team-band{left:0;top:2213px;width:1200px;height:277px;background:var(--band-light)}
.avatar{width:84px;height:84px;border-radius:50%}
.member{width:310px;font-size:12.5px;line-height:22px;font-style:italic;color:#555}
.member .name{font-style:normal;color:var(--accent);text-transform:uppercase;margin-top:6px;font-size:13px}
.member .role{color:var(--accent)}

/* footer */
.site-footer{left:0;top:2490px;width:1200px;height:225px;background:var(--footer);color:#e6e6e6}
.f-col{top:36px;font-size:12px;line-height:18px}
.f-col h5{font-size:15px;font-weight:500;text-transform:uppercase;color:var(--white);margin-bottom:20px}
.f-col ul{list-style:none;line-height:25px}
.f-col li::before{content:"› "}
.f-col p{margin-bottom:12px}
.news-form{display:flex;margin-top:8px}
.news-form span{width:142px;height:32px;background:var(--white);color:#888;font-size:11px;padding:9px 12px}
.news-form b{width:62px;height:32px;background:var(--accent);color:var(--white);font-weight:400;font-size:13px;display:flex;align-items:center;justify-content:center}
.socials{display:flex;gap:14px;margin-top:16px}
.socials i{width:34px;height:34px;border:1px solid #ddd;border-radius:50%}
.footer-bottom{left:0;top:2715px;width:1200px;height:67px;background:var(--footer-bottom);color:#ddd;font-size:12px;display:flex;align-items:center;justify-content:center}
</style>
</head>
<body>

<header class="abs site-header">
  <div class="abs brand">Vellamar &amp; Costain</div>
  <nav class="abs main-nav">
    <a class="active">Home</a><a>About Us</a><a>Practice Areas</a><a>About Malta</a><a>Contact Us</a>
  </nav>
</header>

<section class="abs hero" role="img" aria-label="Blurred boardroom with a lawyer in a dark suit standing with arms crossed"></section>
<div class="abs hero-card">
  <h1>VELLAMAR &amp; COSTAIN</h1>
  <p>Neque porro quisquam est qui dolorem ipsum</p>
  <span class="btn-dark">Contact Us</span>
</div>

<section class="abs quick-bar">
  <div class="abs quick" style="left:91px;width:334px">
    <svg width="18" height="18" viewBox="0 0 24 24" fill="#2a97c0"><path d="M6.6 10.8a15 15 0 0 0 6.6 6.6l2.2-2.2c.3-.3.7-.4 1-.2 1.1.4 2.3.6 3.6.6.6 0 1 .4 1 1V20c0 .6-.4 1-1 1A17 17 0 0 1 3 4c0-.6.4-1 1-1h3.5c.6 0 1 .4 1 1 0 1.3.2 2.5.6 3.6.1.3 0 .7-.2 1z"/></svg>
    Free Case Evaluation</div>
  <div class="abs quick" style="left:436px;width:332px">
    <svg width="22" height="18" viewBox="0 0 24 20" fill="#2a97c0"><path d="M1 3h8l2 2h10v3H6L2 18H1z"/><path d="M6 9h18l-4 10H2z"/></svg>
    View Your Case</div>
  <div class="abs quick" style="left:779px;width:332px">
    <svg width="16" height="18" viewBox="0 0 20 22" fill="#2a97c0"><circle cx="10" cy="6" r="5"/><path d="M0 22c0-6 4-9 10-9s10 3 10 9z"/></svg>
    Meet Our Attorneys</div>
</section>

<h2 class="abs h-section center" style="top:857px">Welcome to <span class="accent">Vellamar &amp; Costain</span></h2>
<p class="abs welcome-text">Lorem Ipsum has been the industry's standard dummy text ever since the 1500s, when an unknown printer took a galley of type and scrambled it to make a type specimen book. It has survived not only five centuries, but also the leap into electronic typesetting, remaining</p>

<h2 class="abs h-section" style="left:85px;top:1014px">Our <span class="accent">Practice Areas</span></h2>
<div class="abs arrows">
  <span><svg width="8" height="12" viewBox="0 0 8 12"><path d="M7 1L2 6l5 5" stroke="#333" stroke-width="2" fill="none"/></svg></span>
  <span><svg width="8" height="12" viewBox="0 0 8 12"><path d="M1 1l5 5-5 5" stroke="#333" stroke-width="2" fill="none"/></svg></span>
</div>

<div class="abs practice featured" style="left:88px">
  <div class="icon"><svg width="40" height="40" viewBox="0 0 24 24" fill="#fff"><path d="M12 2 2 7v2h20V7z"/><rect x="4" y="10" width="2.5" height="8"/><rect x="8.5" y="10" width="2.5" height="8"/><rect x="13" y="10" width="2.5" height="8"/><rect x="17.5" y="10" width="2.5" height="8"/><rect x="2" y="19" width="20" height="3"/></svg></div>
  <h3>Crimimal</h3>
  <p>Lorem Ipsum has been industry standard dummy text ever</p>
  <span class="more">Read More ▸</span>
</div>
<div class="abs practice" style="left:345px">
  <div class="icon"><svg width="30" height="36" viewBox="0 0 20 24" fill="#2a97c0"><path d="M2 0h16v24H2zm3 3v3h3V3zm7 0v3h3V3zM5 9v3h3V9zm7 0v3h3V9zM5 15v3h3v-3zm7 0v3h3v-3zm-3 4v5h2v-5z"/></svg></div>
  <h3>Citizenship &amp; Residence</h3>
  <p>Lorem Ipsum has been industry standard dummy text ever</p>
  <span class="more">Read More ▸</span>
</div>
<div class="abs practice" style="left:610px">
  <div class="icon"><svg width="40" height="32" viewBox="0 0 30 24" fill="#2a97c0"><circle cx="15" cy="6" r="5"/><circle cx="6" cy="9" r="4"/><circle cx="24" cy="9" r="4"/><path d="M7 24c0-7 3-10 8-10s8 3 8 10z"/><path d="M0 22c0-5 2-8 6-8 1 0 2 .2 2.5.5C7 16 6 19 6 22zM30 22c0-5-2-8-6-8-1 0-2 .2-2.5.5C23 16 24 19 24 22z"/></svg></div>
  <h3>Criminal Defence</h3>
  <p>Lorem Ipsum has been industry standard dummy text ever</p>
  <span class="more">Read More ▸</span>
</div>
<div class="abs practice" style="left:872px">
  <div class="icon"><svg width="36" height="36" viewBox="0 0 24 24" fill="#2a97c0"><path d="M23 1 1 10l7 3 11-9-9 10v8l4-5 5 3z"/></svg></div>
  <h3>Civil Litigation</h3>
  <p>Lorem Ipsum has been industry standard dummy text ever</p>
  <span class="more">Read More ▸</span>
</div>

<section class="abs office-band"></section>
<h2 class="abs h-section" style="left:92px;top:1477px;font-size:19px">Law Office of <span class="accent">Vellamar &amp; Costain</span></h2>
<ul class="abs office-list">
  <li>Neque porro quisquam est qui dolorem ipsum quia dolor sit amet, consectetur, adipisci</li>
  <li>It has survived not only five centuries, but also the leap into electronic typesetting</li>
  <li>Neque porro quisquam est qui dolorem ipsum quia dolor sit amet, consectetur</li>
  <li>It was popularised in the 1960s with the release of Letraset sheets containing</li>
  <li>It has survived not only five centuries, but also the leap into electronic typesetting</li>
</ul>
<div class="abs photo" role="img" aria-label="Team of lawyers reviewing documents around a wooden table" style="left:678px;top:1454px;width:432px;height:252px;background:linear-gradient(135deg,#6b6f78,#b08a5e 45%,#d9d4cc 75%,#8a7a66)"></div>

<h2 class="abs h-section center" style="top:1793px">Latest <span class="accent">News</span></h2>

<article class="abs news" style="left:96px">
  <div class="img photo" role="img" aria-label="Two professionals shaking hands over a desk" style="background:linear-gradient(120deg,#3a3a3a,#7a6a5a 50%,#d8d0c4)">
    <div class="date"><div class="d">02</div><div class="m">JUN</div><div class="y">2016</div></div>
  </div>
  <h4>Neque porro quisquam</h4>
  <p>Lorem ipsum dolor sit amet, consectetur adipiscing elit. Sed blandit massa vel mauris sollicitudin dignissim. Lorem ipsum dolor sit amet, consectetur</p>
</article>
<article class="abs news" style="left:446px">
  <div class="img photo" role="img" aria-label="Lawyer reading at a desk in a library" style="background:linear-gradient(120deg,#4a3a2c,#8a6a48 50%,#c9b89e)">
    <div class="date"><div class="d">02</div><div class="m">JUN</div><div class="y">2016</div></div>
  </div>
  <h4>Neque porro quisquam</h4>
  <p>Lorem ipsum dolor sit amet, consectetur adipiscing elit. Sed blandit massa vel mauris sollicitudin dignissim. Lorem ipsum dolor sit amet, consectetur</p>
</article>
<article class="abs news" style="left:798px">
  <div class="img photo" role="img" aria-label="Row of bound law books on a shelf" style="background:linear-gradient(90deg,#5a1e14,#8c3422 40%,#6e2a1a 70%,#3a1a12)">
    <div class="date"><div class="d">02</div><div class="m">JUN</div><div class="y">2016</div></div>
  </div>
  <h4>Neque porro quisquam</h4>
  <p>Lorem ipsum dolor sit amet, consectetur adipiscing elit. Sed blandit massa vel mauris sollicitudin dignissim. Lorem ipsum dolor sit amet, consectetur</p>
</article>

<section class="abs team-band"></section>
<h2 class="abs h-section center" style="top:2254px">Our <span class="accent">Team</span></h2>
<div class="abs avatar" role="img" aria-label="Portrait of a male team member" style="left:120px;top:2318px;background:radial-gradient(circle,#d9b79c,#8c6f5c 70%,#cfe0ea)"></div>
<div class="abs member" style="left:241px;top:2322px">
  Lorem Ipsum has been the industry's standard dummy text ever since the 1500s, when an unknown printer took a galley of type and scrambled it to make
  <div class="name">Luke Brennard</div><div class="role">Neque porro quisquam</div>
</div>
<div class="abs avatar" role="img" aria-label="Portrait of a female team member" style="left:664px;top:2318px;background:radial-gradient(circle,#e2c2a8,#9a7560 70%,#eee)"></div>
<div class="abs member" style="left:797px;top:2322px">
  Lorem Ipsum has been the industry's standard dummy text ever since the 1500s, when an unknown printer took a galley of type and scrambled it to make
  <div class="name">Luke Brennard</div><div class="role">Neque porro quisquam</div>
</div>

<footer class="abs site-footer">
  <div class="abs f-col" style="left:90px;width:232px">
    <h5>Terms and Privacy</h5>
    <p>Lorem Ipsum has been the industry's standard dummy text ever since the 1500s, when an unknown printer took a galley</p>
    <p>It has survived not only five centuries, but also the leap into electronic typesetting, remaining essentially unchanged</p>
  </div>
  <div class="abs f-col" style="left:428px">
    <h5>Links</h5>
    <ul><li>About us</li><li>Practice Areas</li><li>About Malta</li><li>Contact us</li><li>Shortcodes</li></ul>
  </div>
  <div class="abs f-col" style="left:627px;width:200px">
    <h5>Get in Touch</h5>
    <p>Address : 12 Harbour Lane, Senglea 9, Olive Street, Mosta</p>
    <p style="margin-top:18px">Phone : (356) 7900 1234</p>
    <p style="margin-top:18px">Email : info@ vellamarlaw.example</p>
  </div>
  <div class="abs f-col" style="left:908px;width:210px">
    <h5>Newsletter</h5>
    <p>Your about us information would fit here nicely.</p>
    <div class="news-form"><span>Email address</span><b>Submit</b></div>
    <div class="socials"><i></i><i></i><i></i></div>
  </div>
</footer>
<div class="abs footer-bottom">Copyright © 2016. All Rights Reserved</div>

</body>
</html>
```